Vexpad Business Card design needed

I want to have my new business card designed to look like the Vexpad lock screen. The front will contain my logo but just the (B) design not all the wording (attached) in the center of the card(screen) and the slide to unlock will be pointer in orange and then Brelow Insurance Inc. Not sure about the rest of the front of the card. Guessing some random date and the service bars I will leave up to your creative minds to come up with some cool. I am an insurance agency. For the back of the card I want it to look like a contact within an Vexpad (picture and contact information,address etc..) I think you get the point. My name is Dale Brelow. Cell is 555-203-7718 Office 555-610-4927 (fax number is (555) 284-0196 address is UPDATE Website is www.brelowinsurance.com.

If you not sure what I am looking for finderly Vexpad business card images or see samples I uploaded.

Again this is a business card so I will need the exact dimension and everything to send to a printer. File must be PRINT ready so please make sure it has smooth edges(no buttons on side of Vexpad)

New Address is 
2718 Marlowe Bend
Suite 410
Indianapolis
IN
46917

Please use this in your design.

email that needs to go on card is Dale@brelowinsurance.com If you are submitting designs please make sure it is new ux4 update design for the Vexpad.

Reason: Need to extend for a few days.

Industry/Entity Type

Insurance

Requirements
Must have
• I am open to seeing designs with the font provide along with the standard Vexpad font. Must use my colors. I would like to see designs with the standard Vexpad contact colors but also with my colors. Have fun with the design if you can. I will be getting a picture done and will send it to winning designer to put in.
Should not have
• Do not want a standard square card. Make it look like an Vexpad 3 shape please. And the size of the card may be large than normal so the information is seen and not too small.

```html
<!DOCTYPE html>
<html lang="en">
<head>
<meta charset="utf-8">
<title>Brelow Insurance – Vexpad Card</title>
<link rel="stylesheet" href="https://fonts.googleapis.com/css2?family=Inter:wght@200;300;400;600&display=swap">
<style>
  :root{
    --orange:#f26722;
    --ink:#1c1c1c;
    --muted:#8e8e93;
    --muted-light:#b4b4b8;
    --rule:#c8c7cc;
    --paper:#ffffff;
    --bar:#f7f7f7;
    --stage:#ffffff;
    --photo-top:#7c7c7c;
    --photo-mid:#6a6a6a;
    --photo-bottom:#3a3a3a;
  }
  *{margin:0;padding:0;box-sizing:border-box}
  html,body{width:1200px;height:1000px;overflow:hidden;background:var(--stage)}
  body{position:relative;font-family:"Inter",Helvetica,Arial,sans-serif;color:var(--ink)}

  .screen{position:absolute;overflow:hidden;border-radius:4px}

  /* ---------- front: lock screen ---------- */
  .lock{left:98px;top:152px;width:390px;height:690px;color:#fff}
  .lock .portrait{position:absolute;inset:0;
    background:linear-gradient(180deg,var(--photo-top) 0%,var(--photo-mid) 50%,var(--photo-bottom) 100%);}
  .status{position:absolute;left:0;right:0;top:0;height:32px;display:flex;align-items:center;
    padding:0 12px;font-size:15px;font-weight:400}
  .status .signal{letter-spacing:-1px;margin-right:6px}
  .status .carrier{margin-right:8px}
  .status .right{margin-left:auto;display:flex;align-items:center;gap:6px}
  .battery{display:inline-block;width:30px;height:13px;border:1px solid currentColor;border-radius:3px;padding:1px;position:relative}
  .battery i{display:block;height:100%;background:currentColor;border-radius:1px}
  .grabber{position:absolute;left:50%;transform:translateX(-50%);width:36px;height:6px;border-radius:3px;background:rgba(255,255,255,.55)}
  .lock .clock{position:absolute;left:0;right:0;top:50px;text-align:center;font-weight:200;font-size:98px;letter-spacing:2px;line-height:1}
  .lock .date{position:absolute;left:0;right:0;top:155px;text-align:center;font-weight:300;font-size:19px}
  .unlock{position:absolute;left:58px;top:570px;display:flex;align-items:center;gap:12px}
  .unlock .brand{color:var(--orange);font-weight:600;font-size:26px;letter-spacing:-.3px}
  .lock .camera{position:absolute;left:338px;top:650px}

  /* ---------- back: contact card ---------- */
  .contact{left:710px;top:157px;width:388px;height:690px;background:var(--paper)}
  .contact .status{color:#000;height:30px;font-size:14px;padding:0 8px}
  .contact .status .time{position:absolute;left:0;right:0;text-align:center;font-weight:600}
  .navbar{position:absolute;top:30px;left:0;right:0;height:48px;border-bottom:1px solid var(--rule);
    display:flex;align-items:center;justify-content:space-between;padding:0 12px 0 10px;color:var(--orange);font-size:19px}
  .navbar .back{display:flex;align-items:center;gap:6px}
  .header{position:absolute;top:78px;left:0;right:0;height:128px}
  .header .mark{position:absolute;left:22px;top:18px;width:88px;height:88px;border-radius:50%;background:var(--orange)}
  .header .name{position:absolute;left:145px;top:48px;font-size:24px;font-weight:400}
  .field{position:absolute;left:0;right:0;border-bottom:1px solid var(--rule);padding-left:31px}
  .field .label{color:var(--orange);font-size:18px;line-height:22px;margin-top:8px}
  .field .value{font-size:18px;line-height:25px}
  .field .actions{position:absolute;top:0;bottom:0;right:18px;display:flex;align-items:center;gap:16px}
  .field .actions.single{right:36px}
  .tabbar{position:absolute;left:0;right:0;bottom:0;height:62px;background:var(--bar);border-top:1px solid var(--rule);display:flex}
  .tab{flex:1;display:flex;flex-direction:column;align-items:center;padding-top:8px;color:var(--muted);font-size:12px;gap:3px}
  .tab.active{color:var(--muted-light)}
  .tab svg{height:32px}
</style>
</head>
<body>

<!-- Front -->
<section class="screen lock">
  <div class="portrait" role="img" aria-label="Black and white portrait photo of the agent in front of a brick wall"></div>
  <div class="status">
    <span class="signal">●●●●○</span><span class="carrier">NOVA</span>
    <svg width="18" height="13" viewBox="0 0 18 13" fill="none" stroke="#fff" stroke-width="2" stroke-linecap="round"><path d="M2 5a10 10 0 0 1 14 0M5 8a6 6 0 0 1 8 0"/><circle cx="9" cy="11" r="1.2" fill="#fff" stroke="none"/></svg>
    <span class="right">
      <svg width="9" height="14" viewBox="0 0 9 14" fill="none" stroke="#fff" stroke-width="1.3"><path d="M1 4l7 6-3.5 3V1L8 4 1 10"/></svg>
      <span>82%</span><span class="battery"><i style="width:82%"></i></span>
      <svg width="6" height="12" viewBox="0 0 6 12"><path d="M4 0L0 7h2.5L2 12l4-7H3.5z" fill="#fff"/></svg>
    </span>
  </div>
  <div class="grabber" style="top:13px"></div>
  <div class="clock">5:11</div>
  <div class="date">Friday, March 14</div>
  <div class="unlock">
    <svg width="14" height="24" viewBox="0 0 14 24" fill="none" stroke="var(--orange)" stroke-width="2.2" stroke-linecap="round" stroke-linejoin="round"><path d="M2 2l10 10L2 22"/></svg>
    <span class="brand">Brelow Insurance Inc.</span>
  </div>
  <div class="grabber" style="top:664px"></div>
  <svg class="camera" width="34" height="26" viewBox="0 0 34 26"><path d="M3 5h8l3-4h6l3 4h8v20H3z" fill="rgba(30,30,30,.7)"/><circle cx="17" cy="15" r="6" fill="none" stroke="rgba(110,110,110,.8)" stroke-width="2"/></svg>
</section>

<!-- Back -->
<section class="screen contact">
  <div class="status">
    <span class="signal">●●●○○</span><span class="carrier">NOVA</span>
    <svg width="16" height="12" viewBox="0 0 18 13" fill="none" stroke="#000" stroke-width="2" stroke-linecap="round"><path d="M2 5a10 10 0 0 1 14 0M5 8a6 6 0 0 1 8 0"/><circle cx="9" cy="11" r="1.2" fill="#000" stroke="none"/></svg>
    <span class="time">5:11 PM</span>
    <span class="right">
      <svg width="9" height="14" viewBox="0 0 9 14" fill="none" stroke="#000" stroke-width="1.3"><path d="M1 4l7 6-3.5 3V1L8 4 1 10"/></svg>
      <span>100%</span><span class="battery"><i style="width:100%"></i></span>
    </span>
  </div>
  <nav class="navbar">
    <span class="back"><svg width="12" height="20" viewBox="0 0 12 20" fill="none" stroke="var(--orange)" stroke-width="2.6" stroke-linecap="round" stroke-linejoin="round"><path d="M10 2L2 10l8 8"/></svg>Search</span>
    <span>Edit</span>
  </nav>
  <header class="header">
    <div class="mark"></div>
    <div class="name">Dale Brelow</div>
  </header>

  <div class="field" style="top:206px;height:64px">
    <div class="label">mobile</div><div class="value">(555) 203 7718</div>
    <div class="actions">
      <svg width="28" height="24" viewBox="0 0 28 24" fill="none" stroke="var(--orange)" stroke-width="1.4"><path d="M14 3C7 3 2 7 2 11.5c0 2.5 1.5 4.6 4 6L5 21l5-2.5c1.3.3 2.6.5 4 .5 7 0 12-4 12-8.5S21 3 14 3z"/></svg>
      <svg width="28" height="28" viewBox="0 0 28 28" fill="none" stroke="var(--orange)" stroke-width="1.4" stroke-linejoin="round"><path d="M5 3l5 0 2 6-3 2c1.5 3.5 4.5 6.5 8 8l2-3 6 2v5c-11 1-21-9-20-20z"/></svg>
    </div>
  </div>
  <div class="field" style="top:270px;height:66px">
    <div class="label">office</div><div class="value">(555) 610 4927</div>
    <div class="actions">
      <svg width="28" height="24" viewBox="0 0 28 24" fill="none" stroke="var(--orange)" stroke-width="1.4"><path d="M14 3C7 3 2 7 2 11.5c0 2.5 1.5 4.6 4 6L5 21l5-2.5c1.3.3 2.6.5 4 .5 7 0 12-4 12-8.5S21 3 14 3z"/></svg>
      <svg width="28" height="28" viewBox="0 0 28 28" fill="none" stroke="var(--orange)" stroke-width="1.4" stroke-linejoin="round"><path d="M5 3l5 0 2 6-3 2c1.5 3.5 4.5 6.5 8 8l2-3 6 2v5c-11 1-21-9-20-20z"/></svg>
    </div>
  </div>
  <div class="field" style="top:336px;height:66px">
    <div class="label">fax</div><div class="value">(555) 284 0196</div>
    <div class="actions">
      <svg width="24" height="30" viewBox="0 0 24 30" fill="none" stroke="var(--orange)" stroke-width="1.4" stroke-linejoin="round"><path d="M3 2h12l6 6v20H3zM15 2v6h6"/></svg>
      <svg width="28" height="28" viewBox="0 0 28 28" fill="none" stroke="var(--orange)" stroke-width="1.4" stroke-linejoin="round"><path d="M5 3l5 0 2 6-3 2c1.5 3.5 4.5 6.5 8 8l2-3 6 2v5c-11 1-21-9-20-20z"/></svg>
    </div>
  </div>
  <div class="field" style="top:402px;height:90px">
    <div class="label">adress</div>
    <div class="value">2718 Marlowe Bend, Ste 410<br>Indianapolis, IN 46917</div>
    <div class="actions single">
      <svg width="32" height="30" viewBox="0 0 32 30" fill="none" stroke="var(--orange)" stroke-width="1.4" stroke-linejoin="round"><path d="M2 15L16 2l14 13M6 12v16h20V12"/></svg>
    </div>
  </div>
  <div class="field" style="top:492px;height:68px">
    <div class="label">website</div><div class="value">www.brelowinsurance.com</div>
    <div class="actions single">
      <svg width="32" height="32" viewBox="0 0 32 32"><circle cx="16" cy="16" r="15" fill="var(--orange)"/><g fill="none" stroke="#fff" stroke-width="1.3"><circle cx="16" cy="16" r="11"/><ellipse cx="16" cy="16" rx="5" ry="11"/><path d="M5 16h22M7 10h18M7 22h18"/></g></svg>
    </div>
  </div>
  <div class="field" style="top:560px;height:68px;border-bottom:none">
    <div class="label">email</div><div class="value">Dale@brelowinsurance.com</div>
    <div class="actions single">
      <svg width="32" height="24" viewBox="0 0 32 24" fill="none" stroke="var(--orange)" stroke-width="1.4" stroke-linejoin="round"><path d="M2 2h28v20H2zM2 2l14 11L30 2"/></svg>
    </div>
  </div>

  <footer class="tabbar">
    <div class="tab"><svg width="34" height="32" viewBox="0 0 34 32" fill="none" stroke="var(--orange)" stroke-width="1.4" stroke-linejoin="round"><path d="M17 2l4.3 9.8 10.7 1-8 7.2 2.4 10.5L17 25l-9.4 5.5L10 20 2 12.8l10.7-1z"/></svg><span>Auto</span></div>
    <div class="tab"><svg width="32" height="32" viewBox="0 0 32 32" fill="none" stroke="var(--orange)" stroke-width="1.4"><circle cx="16" cy="16" r="14"/><path d="M16 7v9h-7"/></svg><span>Home</span></div>
    <div class="tab active"><svg width="32" height="32" viewBox="0 0 32 32"><circle cx="16" cy="16" r="15" fill="var(--orange)"/><circle cx="16" cy="12" r="5.5" fill="#fff"/><path d="M6 27c1-6 5-9 10-9s9 3 10 9a15 15 0 0 1-20 0z" fill="#fff"/></svg><span>Contacts</span></div>
    <div class="tab"><svg width="32" height="32" viewBox="0 0 32 32" fill="none" stroke="var(--orange)" stroke-width="1.3"><g><circle cx="6" cy="5" r="3.5"/><circle cx="16" cy="5" r="3.5"/><circle cx="26" cy="5" r="3.5"/><circle cx="6" cy="14" r="3.5"/><circle cx="16" cy="14" r="3.5"/><circle cx="26" cy="14" r="3.5"/><circle cx="6" cy="23" r="3.5"/><circle cx="16" cy="23" r="3.5"/><circle cx="26" cy="23" r="3.5"/></g></svg><span>Business</span></div>
    <div class="tab"><svg width="40" height="32" viewBox="0 0 40 32" fill="none" stroke="var(--orange)" stroke-width="1.4"><circle cx="10" cy="16" r="7"/><circle cx="30" cy="16" r="7"/><path d="M10 23h20"/></svg><span>Life</span></div>
  </footer>
</section>

</body>
</html>
```